Fish Farm needing 3 - Fold Flyer / Price List designed

We are looking for a new Price List for our Fish Farm. I have attached an example of the basic info that needs in the flyer. We want the flyer to be a 3 fold page. Anything that is on our website, you can use for ideas. There are some pictures on there that can be photoshopped into the flyer. Do not use any photos from any other sites. We are looking for something professional but fun and exciting! I have also attached our business logo. We tend to stay with the blues and greens for colors. Let's get started....
Updates

Need extra days to review

Contact Information for Business Card

We are needing a business card with our new logo on it. We also need our address, phone numbers, email address, and website listed. Please view our website for more ideas.

Colors

Designer to choose colors to be used in the design.

```html
<!DOCTYPE html>
<html lang="en">
<head>
<meta charset="utf-8">
<title>Brookline Fish Farm – Price List</title>
<link rel="stylesheet" href="https://fonts.googleapis.com/css2?family=Roboto+Condensed:wght@400;700&family=PT+Sans:wght@400;700&family=PT+Serif:ital,wght@1,700&display=swap">
<style>
  :root {
    --navy: #1c2e7c;
    --navy-deep: #16246a;
    --blue: #2b63c9;
    --blue-bright: #3f8fe2;
    --blue-pale: #cfe3f7;
    --panel: #eceef2;
    --ink: #1a1a1a;
    --white: #ffffff;
  }
  * { margin: 0; padding: 0; box-sizing: border-box; }
  html, body { width: 1200px; height: 848px; overflow: hidden; background: var(--white); }
  .flyer {
    position: relative; width: 1200px; height: 848px; overflow: hidden;
    font-family: "PT Sans", Arial, sans-serif; color: var(--ink);
    background: var(--white);
  }
  .backdrop { position: absolute; inset: 0; }

  .block { position: absolute; }
  .heading {
    font-family: "Roboto Condensed", "Arial Narrow", sans-serif;
    font-weight: 700; color: var(--navy); font-size: 31px; line-height: 1;
    text-transform: uppercase; letter-spacing: 0.2px; white-space: nowrap;
  }
  .rule {
    position: absolute; height: 4px;
    background: linear-gradient(90deg, var(--navy) 0%, var(--blue) 70%, rgba(43,99,201,0) 100%);
  }
  .sub {
    font-family: "Roboto Condensed", "Arial Narrow", sans-serif;
    font-weight: 700; color: var(--blue); font-size: 20px; white-space: nowrap;
  }
  .row { position: absolute; font-size: 18px; white-space: nowrap; line-height: 1; }
  .row span { position: absolute; top: 0; }
  .col-head { color: var(--blue); font-family: "Roboto Condensed", sans-serif; font-weight: 700; font-size: 19px; }
  .centered { text-align: center; }

  .pill {
    position: absolute; top: 31px; height: 36px; border-radius: 18px 18px 0 0;
    background: var(--navy); color: var(--white);
    font-family: "Roboto Condensed", sans-serif; font-weight: 700; font-size: 21px;
    display: flex; align-items: center; justify-content: center;
  }

  .promo {
    position: absolute; left: 528px; top: 640px; width: 214px; height: 86px;
    transform: rotate(-13deg);
    background: linear-gradient(180deg, var(--blue-bright), var(--blue));
    border-radius: 4px; box-shadow: 0 3px 8px rgba(0,0,0,0.25);
    color: var(--white); font-family: "Roboto Condensed", sans-serif; font-weight: 700;
    font-size: 25px; line-height: 1.05; text-align: center; text-transform: uppercase;
    display: flex; align-items: center; justify-content: center;
  }

  .brand {
    position: absolute; left: 862px; top: 728px; width: 320px;
    display: flex; align-items: center; gap: 10px;
    font-family: "Roboto Condensed", sans-serif; font-weight: 700; color: var(--navy);
    font-size: 27px; line-height: 1; text-transform: uppercase; white-space: nowrap;
  }
  .brand-dot { flex: none; width: 20px; height: 20px; border-radius: 50%; background: var(--blue); }

  .footer {
    position: absolute; left: 0; bottom: 0; width: 1200px; height: 67px;
    font-family: "PT Serif", Georgia, serif; font-style: italic; font-weight: 700; color: var(--white);
  }
  .footer-note { position: absolute; left: 22px; top: 20px; font-size: 20px; }
  .footer-terms { position: absolute; left: 635px; top: 20px; font-size: 20px; letter-spacing: 0.3px; }
</style>
</head>
<body>
<main class="flyer">

  <svg class="backdrop" width="1200" height="848" viewBox="0 0 1200 848" aria-hidden="true">
    <defs>
      <linearGradient id="waveTop" x1="0" y1="0" x2="1" y2="0">
        <stop offset="0" stop-color="#2b63c9"/><stop offset="1" stop-color="#3f8fe2"/>
      </linearGradient>
      <linearGradient id="waveSea" x1="0" y1="0" x2="1" y2="0">
        <stop offset="0" stop-color="#7fb8ee"/><stop offset="1" stop-color="#2b63c9"/>
      </linearGradient>
    </defs>
    <rect class="side-panel" x="0" y="0" width="405" height="781" fill="#eceef2"/>
    <path d="M0 0 H430 C380 40 300 62 0 80 Z" fill="#cfe3f7"/>
    <path d="M0 0 H410 C360 30 270 52 0 62 Z" fill="url(#waveTop)"/>
    <path d="M420 0 C470 20 560 30 700 0 Z" fill="#e3eefa"/>
    <path d="M0 740 C120 710 240 700 405 720 V781 H0 Z" fill="#cfe3f7"/>
    <path d="M210 781 C520 760 820 700 1200 632 V781 Z" fill="#cfe3f7"/>
    <path d="M380 781 C680 768 930 715 1200 668 V781 Z" fill="url(#waveSea)"/>
    <path d="M560 781 C820 776 1010 740 1200 712 V781 Z" fill="#2b63c9"/>
    <polygon points="0,781 640,781 612,848 0,848" fill="#2b63c9"/>
    <polygon points="640,781 1200,781 1200,848 612,848" fill="#16246a"/>
  </svg>

  <!-- Left column -->
  <div class="pill" style="left:21px;width:82px;">Size</div>
  <div class="pill" style="left:117px;width:80px;">Each</div>
  <div class="pill" style="left:211px;width:81px;">1000</div>
  <div class="pill" style="left:306px;width:79px;">3000</div>

  <section class="block" style="left:21px;top:83px;">
    <h2 class="heading">Hybrid Bluegill</h2>
  </section>
  <div class="rule" style="left:0;top:114px;width:405px;"></div>
  <p class="sub block" style="left:0;top:122px;width:405px;text-align:center;">(HYBRID SUNFISH)</p>
  <div class="row" style="left:21px;top:160px;"><span>1-3 Inch</span><span style="left:114px">50¢</span><span style="left:210px">45¢</span><span style="left:305px">40¢</span></div>
  <div class="row" style="left:21px;top:190px;"><span>3-5 Inch</span><span style="left:114px">80¢</span><span style="left:210px">75¢</span></div>
  <div class="row" style="left:21px;top:220px;"><span>*5-7 Inch</span><span style="left:106px">$1.75</span></div>

  <section class="block" style="left:21px;top:251px;"><h2 class="heading">Regular Bluegill</h2></section>
  <div class="rule" style="left:0;top:285px;width:405px;"></div>
  <div class="row" style="left:21px;top:306px;"><span>1-3 Inch</span><span style="left:114px">50¢</span><span style="left:210px">45¢</span></div>
  <div class="row" style="left:21px;top:336px;"><span>*3-5 Inch</span><span style="left:114px">80¢</span><span style="left:210px">75¢</span></div>

  <section class="block" style="left:21px;top:363px;"><h2 class="heading">Redear Sunfish</h2></section>
  <div class="rule" style="left:0;top:396px;width:405px;"></div>
  <div class="row" style="left:21px;top:417px;"><span>1-3 Inch</span><span style="left:114px">50¢</span><span style="left:210px">45¢</span></div>
  <div class="row" style="left:21px;top:447px;"><span>3-4 Inch</span><span style="left:114px">75¢</span><span style="left:210px">70¢</span></div>
  <div class="row" style="left:21px;top:477px;"><span>*4-5 Inch</span><span style="left:106px">$1.00</span><span style="left:210px">95¢</span></div>

  <section class="block" style="left:21px;top:520px;"><h2 class="heading">Largemouth Bass</h2></section>
  <div class="rule" style="left:0;top:553px;width:405px;"></div>
  <div class="row" style="left:21px;top:574px;"><span>3 Inch</span><span style="left:104px">$1.10</span></div>
  <div class="row" style="left:21px;top:602px;"><span>3-4 Inch</span><span style="left:104px">$1.20</span></div>
  <div class="row" style="left:21px;top:632px;"><span>*4-6 Inch</span><span style="left:104px">$1.95</span></div>
  <div class="row" style="left:21px;top:661px;"><span>*6-8 Inch</span><span style="left:104px">$2.75</span></div>

  <section class="block" style="left:21px;top:687px;"><h2 class="heading">Channel Catfish</h2></section>
  <div class="rule" style="left:0;top:720px;width:405px;"></div>
  <div class="row" style="left:21px;top:745px;"><span>6-8 Inch</span><span style="left:114px">65¢</span><span style="left:210px">60¢</span></div>

  <!-- Middle column -->
  <section class="block centered" style="left:420px;top:37px;width:355px;">
    <h2 class="heading" style="font-size:34px;line-height:1.08;">Triploid<br>Grass Carp</h2>
  </section>
  <div class="rule" style="left:406px;top:114px;width:290px;"></div>
  <p class="sub block" style="left:420px;top:124px;width:355px;text-align:center;">(Indiana Prices)</p>
  <div class="row" style="left:442px;top:160px;font-size:17px;"><span>8-11 Inch</span><span style="left:235px">Minimum 5</span></div>
  <div class="row" style="left:442px;top:185px;font-size:17px;"><span>5-24 Grass Carp</span><span style="left:235px">$16.00 each</span></div>
  <div class="row" style="left:442px;top:209px;font-size:17px;"><span>25-49 Grass Carp</span><span style="left:235px">$15.00 each</span></div>
  <div class="row" style="left:442px;top:233px;font-size:17px;"><span>50-99 Grass Carp</span><span style="left:235px">$14.00 each</span></div>
  <div class="row" style="left:442px;top:258px;font-size:17px;"><span>100+ Grass Carp</span><span style="left:235px">Inquire</span></div>

  <section class="block" style="left:425px;top:292px;"><h2 class="heading">Albino Catfish</h2></section>
  <div class="rule" style="left:406px;top:327px;width:290px;"></div>
  <p class="sub block" style="left:492px;top:338px;">(March &amp; April)</p>
  <div class="row col-head" style="left:463px;top:369px;"><span>Size</span><span style="left:170px">Each</span></div>
  <div class="row" style="left:437px;top:390px;"><span>5-8 Inch</span><span style="left:202px">$1.20</span></div>

  <section class="block" style="left:425px;top:428px;"><h2 class="heading">Black Crappie</h2></section>
  <div class="rule" style="left:406px;top:461px;width:290px;"></div>
  <p class="sub block" style="left:492px;top:471px;">(March &amp; April)</p>
  <div class="row col-head" style="left:463px;top:501px;"><span>Size</span><span style="left:170px">Each</span></div>
  <div class="row" style="left:437px;top:523px;"><span>3-5 Inch</span><span style="left:202px">$1.10</span></div>

  <section class="block" style="left:425px;top:566px;"><h2 class="heading">Fathead Minnows</h2></section>
  <div class="rule" style="left:406px;top:600px;width:340px;"></div>
  <div class="row" style="left:425px;top:617px;font-size:17px;"><span>$36.00 per thousand</span></div>
  <div class="row" style="left:425px;top:638px;font-size:17px;"><span>($9.00 per lb.)</span></div>

  <div class="promo">Butterfly Koi<br>Also Available!</div>

  <!-- Right column -->
  <section class="block" style="left:858px;top:21px;"><h2 class="heading">Golden Shiners</h2></section>
  <div class="rule" style="left:855px;top:57px;width:345px;"></div>
  <p class="sub block" style="left:858px;top:64px;">(Delivery Only – Minimum 50 lb.)</p>
  <div class="row" style="left:858px;top:104px;"><span>50-99 lb.</span><span style="left:178px">$8.00 lb.</span></div>
  <div class="row" style="left:858px;top:139px;"><span>100+ lb.</span><span style="left:178px">$7.50 lb.</span></div>

  <section class="block" style="left:858px;top:167px;"><h2 class="heading">Floating Fish Food</h2></section>
  <div class="rule" style="left:855px;top:200px;width:345px;"></div>
  <div class="block" style="left:860px;top:216px;width:330px;text-align:center;font-size:17px;line-height:26px;">
    <p>Starter Size (50 lb. Bag)</p>
    <p>41% Protein</p>
    <p>Market Price – Inquire</p>
    <p>(Only Available at Farm)</p>
  </div>

  <section class="block" style="left:858px;top:316px;"><h2 class="heading">Tilapia</h2></section>
  <div class="rule" style="left:855px;top:349px;width:345px;"></div>
  <p class="sub block" style="left:858px;top:361px;font-size:23px;">(May 15 – June 30)</p>
  <div class="row" style="left:912px;top:392px;font-size:17px;"><span>5-10 Tilapia per lb.</span></div>
  <div class="row" style="left:866px;top:423px;font-size:17px;"><span>1-25 lb.</span><span style="left:163px">$15.00 lb.</span></div>
  <div class="row" style="left:866px;top:446px;font-size:17px;"><span>26-40 lb.</span><span style="left:163px">$14.00 lb.</span></div>
  <div class="row" style="left:866px;top:470px;font-size:17px;"><span>40-50 lb.</span><span style="left:163px">$13.00 lb.</span></div>
  <div class="row" style="left:866px;top:493px;font-size:17px;"><span>50+ lb.</span><span style="left:163px">$12.00 lb.</span></div>

  <section class="block" style="left:858px;top:523px;"><h2 class="heading">Japanese Koi</h2></section>
  <div class="rule" style="left:855px;top:556px;width:345px;"></div>
  <div class="row col-head" style="left:888px;top:573px;font-size:21px;"><span>Size</span><span style="left:160px">Each</span></div>
  <div class="row" style="left:876px;top:600px;"><span>4-5 Inch</span><span style="left:188px">$6.00</span></div>
  <div class="row" style="left:876px;top:628px;"><span>6-8 Inch</span><span style="left:188px">$10.00</span></div>
  <div class="row" style="left:876px;top:657px;"><span>*9-12 Inch</span><span style="left:188px">$15.00</span></div>

  <div class="brand"><span class="brand-dot"></span>Brookline Fish Farm</div>

  <footer class="footer">
    <p class="footer-note">*When Available. Sizes Vary Depending on Time of Year</p>
    <p class="footer-terms">PRICES SUBJECT TO CHANGE WITHOUT NOTICE</p>
  </footer>
</main>
</body>
</html>
```